Website Online Research Solutions

We are a small European high-tech online research company.
With our own state of the art software we run online panels and are conducting reseach for companies. Partly research via our own panel and partly via panels we maintain for our customers.
Our current website is old and outdatet: www.pravelo.nl.
We are in the process to change the content of the site. We want a modern, european and businesslike design for our new website.
Our logo has to stay the same (left uppersite of our website and attached) but can be changed a little to adapt it to the new design of the website. The colors of the site are up to you.
Target Market(s)
Marketeers and researchers of large and middle size companies in all kind of fields.
Industry/Entity Type
Online
Look and feel
Each slider illustrates characteristics of the customer's brand and the style your logo design should communicate.

```html
<!DOCTYPE html>
<html lang="nl">
<head>
<meta charset="utf-8">
<title>Pravelo – Producten</title>
<link href="https://fonts.googleapis.com/css2?family=Open+Sans:ital,wght@0,300;0,400;0,600;0,700;1,300;1,400&display=swap" rel="stylesheet">
<style>
:root{
  --bar:#5f6064;
  --band:#e2e2e2;
  --heading:#5a5a5a;
  --text:#9c9c9c;
  --nav:#7a7a7a;
  --soft:#b5b5b5;
  --panel:#ececec;
  --rule:#e0e0e0;
  --footer:#6d6e72;
  --footer-text:#d0d0d2;
  --white:#ffffff;
  --strong:#8a8a8a;
}
*{margin:0;padding:0;box-sizing:border-box}
html,body{width:1200px;height:1193px;overflow:hidden;background:var(--white)}
body{position:relative;font-family:"Open Sans",sans-serif;color:var(--text);font-size:11px;line-height:17px}
.abs{position:absolute}
.topbar{left:0;top:0;width:1200px;height:7px;background:var(--bar)}
.brand{left:160px;top:30px;display:flex;align-items:center;gap:12px}
.brand-mark{width:56px;height:56px;border:2px solid var(--heading);border-radius:50%}
.brand-name{font-size:26px;font-weight:300;color:var(--heading);letter-spacing:.5px}
.nav{left:552px;top:40px;display:flex;font-size:14.5px;font-weight:300;color:var(--nav)}
.nav a{color:inherit;text-decoration:none}
.nav a:nth-child(1){margin-right:45px}
.nav a:nth-child(2){margin-right:45px}
.nav a:nth-child(3){margin-right:46px;color:var(--soft)}
.nav a:nth-child(4){margin-right:44px}
.nav a:nth-child(5){margin-right:42px}
.band{left:0;top:106px;width:1200px;height:82px;background:var(--band)}
.band-title{left:162px;top:124px;font-size:26px;font-weight:300;color:var(--heading)}
.band-divider{left:302px;top:128px;height:36px;border-left:1px dotted #b9b9b9}
.band-text{left:331px;top:130px;width:480px;font-size:10.5px;color:var(--text)}
h2{font-weight:300;color:var(--heading)}
.h-lg{font-size:20px}
.h-md{font-size:16px}
.lead{left:144px;top:270px;width:590px;font-size:14px;line-height:23px;font-style:italic;font-weight:300;color:var(--soft)}
.shot{left:144px;top:360px;width:329px;height:216px;background:linear-gradient(180deg,#c9c9c9 0,#dcdcdc 14%,#f4f4f4 30%,#eef3f8 100%);border-radius:4px 0 0 0}
.intro{left:518px;top:328px;width:220px;font-size:11px}
.checks{left:144px;top:673px;list-style:none}
.checks li{display:flex;align-items:center;height:25px;font-size:11px}
.checks svg{width:14px;height:12px;margin-right:7px}
.features{left:144px;top:788px;width:590px;height:143px;background:var(--panel);border-radius:5px}
.feature{position:absolute;top:12px}
.feature h3{font-size:14.5px;font-weight:300;color:var(--heading);margin-bottom:5px}
.feature-art{position:absolute;left:5px;top:28px;width:70px;height:72px;border-radius:8px}
.feature p{position:absolute;left:90px;top:26px;width:180px;font-size:10.5px}
.side-box{left:784px;border-left:2px solid var(--rule);border-bottom:2px solid var(--rule);border-radius:0 0 0 6px;width:274px}
.trust-photo{left:805px;top:268px;width:245px;height:97px;background:linear-gradient(120deg,#8f9aa4 0%,#dfe3e7 40%,#c7ced4 70%,#5d646b 100%)}
.quote-mark{left:803px;top:512px;font-size:48px;line-height:48px;color:#c4c4c4;font-family:Georgia,serif}
.quote{left:842px;top:524px;width:215px;font-style:italic;font-size:10.5px}
.cite{left:805px;top:609px;font-weight:700;color:var(--strong);font-size:11px}
.footer{left:0;top:1008px;width:1200px;height:185px;background:radial-gradient(ellipse 320px 120px at 260px 30px,#85868a,transparent),radial-gradient(ellipse 320px 120px at 880px 30px,#85868a,transparent),var(--footer)}
.footer-brand{left:144px;top:1035px;display:flex;align-items:center;gap:8px;color:var(--white)}
.footer-brand .brand-mark{width:40px;height:40px;border-color:var(--footer-text)}
.footer-brand span{font-size:18px;font-weight:300;color:var(--footer-text)}
.address{left:144px;top:1091px;width:260px;color:var(--footer-text);font-size:11px}
.news-title{left:620px;top:1031px;font-size:20px;font-weight:300;color:var(--white)}
.news{left:620px;top:1063px;width:436px;list-style:none}
.news li{height:28.5px;padding-top:6px;border-bottom:1px dotted #8f9094;color:var(--footer-text);font-size:10.5px;white-space:nowrap}
.news b{font-weight:700;color:#e8e8ea}
</style>
</head>
<body>
<div class="abs topbar"></div>

<header>
  <div class="abs brand"><span class="brand-mark"></span><span class="brand-name">Pravelo</span></div>
  <nav class="abs nav"><a href="#">Home</a><a href="#">Producten</a><a href="#">Demo's</a><a href="#">Media</a><a href="#">Ref</a><a href="#">Contact</a></nav>
</header>

<section>
  <div class="abs band"></div>
  <h1 class="abs band-title" style="font-weight:300">Producten</h1>
  <div class="abs band-divider"></div>
  <p class="abs band-text">Pravelo is gespecialiseerd in online gegevensverzameling en analyse en is werkzaam voor internationale opdrachtgevers. Pravelo is gespecialiseerd in online gegevensverzameling en analyse en is werkzaam…</p>
</section>

<main>
  <h2 class="abs h-lg" style="left:144px;top:232px">Dataverzameling</h2>
  <p class="abs lead">Vragenlijsten die door Pravelo worden geprogrammeerd zijn dynamisch gegenereerde vragenlijsten die in de "look &amp; feel" worden geprogrammeerd van onze klanten en/of de produkten van onze…</p>
  <div class="abs shot" role="img" aria-label="Screenshot of an online analytics dashboard in a browser window"></div>
  <p class="abs intro">Pravelo programmeert vragenlijsten/enquetes voor gegevensverzameling via internet, intranet of via email. Recentelijk hebben we zelfs betrouwbare methoden ontwikkeld voor onderzoek via SMS. De vele honderden onderzoeken die wij hebben geprogrammeerd varieren van eenvoudige onderzoeken via quickpolls met een aantal korte stellingen of banners tot en met complexe (inter)nationale multilinguale monitoren, medewerker&amp;klanttevredenheid onderzoek, usability tests etc. Pravelo programmeert vragenlijsten/enquetes voor….</p>

  <h2 class="abs h-md" style="left:144px;top:595px">Detail services</h2>
  <p class="abs" style="left:144px;top:627px;width:590px">Occaecati cupiditate non provident, similique sunt in culpa qui officia deserunt mollitia animi, id est laborum et dolorum fuga et harum quidem rerum facilis est et expedita distinctio. Nam libero tempore, cum soluta nobis est eligendi optio cumque.</p>
  <ul class="abs checks">
    <li><svg viewBox="0 0 14 12"><path d="M1 6l4 4 8-9" fill="none" stroke="#8d8d8d" stroke-width="2.4" stroke-linecap="round" stroke-linejoin="round"/></svg>Occaecat cupidatat non proident, sunt in culpa qui officia deserunt mollit</li>
    <li><svg viewBox="0 0 14 12"><path d="M1 6l4 4 8-9" fill="none" stroke="#8d8d8d" stroke-width="2.4" stroke-linecap="round" stroke-linejoin="round"/></svg>Neque porro quisquam est, qui dolorem ipsum quia dolor sit amets adipisci velit</li>
    <li><svg viewBox="0 0 14 12"><path d="M1 6l4 4 8-9" fill="none" stroke="#8d8d8d" stroke-width="2.4" stroke-linecap="round" stroke-linejoin="round"/></svg>excepturi sint occaecati cupiditate non provident, similique sunt in officia</li>
    <li><svg viewBox="0 0 14 12"><path d="M1 6l4 4 8-9" fill="none" stroke="#8d8d8d" stroke-width="2.4" stroke-linecap="round" stroke-linejoin="round"/></svg>Temporibus autem quibusdam et aut officiis debitis aut rerum necessitatibus</li>
  </ul>

  <div class="abs features">
    <div class="feature" style="left:19px">
      <h3>Streaming Audio/Video</h3>
      <div class="feature-art" role="img" aria-label="Paint bucket with brush icon" style="background:radial-gradient(circle at 45% 40%,#7fd2e4,#a9b1b7 60%,#ececec 100%)"></div>
      <p>Itaque earum rerum hic tenetur alias sapiente delectus, ut aut reiciendis voluptatibus maiores consequatur aut perferendis doloribus asperiores repellat ducimus blanditiis praesentim</p>
    </div>
    <div class="feature" style="left:309px">
      <h3>V for Tables</h3>
      <div class="feature-art" role="img" aria-label="Metal gears icon" style="background:radial-gradient(circle at 50% 50%,#c4c6c8,#9a9da0 55%,#ececec 100%)"></div>
      <p>Itaque earum rerum hic tenetur alias sapiente delectus, ut aut reiciendis voluptatibus maiores consequatur aut perferendis doloribus asperiores repellat ducimus blanditiis praesentim</p>
    </div>
  </div>
</main>

<aside>
  <div class="abs side-box" style="top:235px;height:222px"></div>
  <h2 class="abs h-lg" style="left:805px;top:232px">Trust your project to us</h2>
  <div class="abs trust-photo" role="img" aria-label="Photo of a ruler and pencil on technical drawings"></div>
  <p class="abs" style="left:805px;top:368px;width:252px;font-size:10.5px">Temporibus autem quibusdam et aut officiis debitis aut rerum necessitatibus saepe eveniet ut et voluptates repudiandae sint et molestiae non recusandae itaque earum rerum hic tenetur a sapiente delectus reiciendis.</p>

  <div class="abs side-box" style="top:490px;height:174px"></div>
  <h2 class="abs h-lg" style="left:805px;top:488px">Client testimonials</h2>
  <div class="abs quote-mark">“</div>
  <p class="abs quote">Pravelo biedt ons een zeer flexibele, snelle en efficiente onderzoekstool. Hiermee sluiten ze uitstekend aan bij de behoeften van onze marketeers.</p>
  <p class="abs cite">Maarten Vellinga - Consumer Intelligence Manager<br>Harlow Fresh Foods</p>
</aside>

<footer>
  <div class="abs footer"></div>
  <div class="abs footer-brand"><span class="brand-mark"></span><span>Pravelo</span></div>
  <p class="abs address">Lindentoren - 12 Keizersgracht 3rd Floor, Utrecht, 3511 AB, Netherlands<br><br>Telp : +31 30 555 0142, Fax : +31 30 555 0143<br>Email : info@pravelo.nl, support@pravelo.nl</p>
  <h2 class="abs news-title">Company News</h2>
  <ul class="abs news">
    <li>Quis autem vel eum iure reprehenderit qui in ea voluptate velit esse - <b>23 May 2010</b></li>
    <li>At vero eos et accusamus et iusto odio dignissimos ducimus qui blanditiis - <b>14 May 2010</b></li>
    <li>Nam libero tempore, cum soluta nobis est eligendi optio cumque nihil impedit - <b>05 May 2010</b></li>
    <li>Temporibus autem quibusdam et aut officiis debitis rerum necessitatibus - <b>22 April 2010</b></li>
  </ul>
</footer>
</body>
</html>
```